Storm Restoration Contractor needs a professional letterhead design

Looking for a professional letterhead design. Not looking for your cheapo MS Word standard ones that are readily available. Dont want it to be cookie cutter look like ones readily available online. We just recently changed our logo and want to freshen up all our documents. Our company handles restoring a property back to a pre-loss condition after a storm damages it. For example, wind, hail, flood, fire losses.

Target Market(s)

Property Owners, Homeowners, Property Owners, Commercial Property Owners, Property Management Companies

Industry/Entity Type

Construction Company

Requirements
Must have
• Professional, Use 1 of 2 logo options
• Storm Restoration, Roofing, Siding, Windows

```html
<!DOCTYPE html>
<html lang="en">
<head>
<meta charset="utf-8">
<title>Northgate Exteriors Letterhead</title>
<link rel="stylesheet" href="https://fonts.googleapis.com/css2?family=Open+Sans:wght@400;600;700&display=swap">
<style>
  :root {
    --backdrop: #e6e7e9;
    --paper: #ffffff;
    --brand-blue: #2468b4;
    --brand-grey: #58595b;
    --text-dark: #2b2b2b;
    --rule: #3d6f93;
  }
  html, body {
    margin: 0;
    padding: 0;
    width: 1200px;
    height: 1200px;
    overflow: hidden;
    background: var(--backdrop);
    font-family: "Open Sans", sans-serif;
  }
  .letterhead {
    position: absolute;
    left: 207px;
    top: 60px;
    width: 786px;
    height: 1080px;
    background: var(--paper);
  }
  .top-band {
    position: absolute;
    left: 0;
    top: 0;
    width: 786px;
    height: 15px;
    display: block;
  }
  .brand {
    position: absolute;
    top: 62px;
    left: 0;
    right: 0;
    display: flex;
    justify-content: center;
    align-items: center;
    gap: 18px;
  }
  .brand-dot {
    width: 70px;
    height: 70px;
    border-radius: 50%;
    background: var(--brand-blue);
  }
  .brand-name {
    color: var(--brand-blue);
    font-weight: 700;
    font-size: 31px;
    line-height: 34px;
    letter-spacing: 1px;
    text-transform: uppercase;
  }
  .footer {
    position: absolute;
    left: 49px;
    right: 49px;
    top: 1020px;
    height: 45px;
    border-top: 1px solid var(--rule);
    border-bottom: 1px solid var(--rule);
    box-sizing: border-box;
    text-align: center;
    font-size: 11.5px;
    line-height: 16px;
    color: var(--text-dark);
    padding-top: 5px;
  }
  .footer .label {
    font-weight: 700;
    color: var(--text-dark);
  }
  .footer .item { margin: 0 4px; }
</style>
</head>
<body>
  <main class="letterhead">
    <svg class="top-band" viewBox="0 0 786 15" aria-hidden="true">
      <rect x="0" y="0" width="786" height="15" fill="var(--brand-grey)"/>
      <polygon points="0,0 403,0 390,15 0,15" fill="var(--brand-blue)"/>
    </svg>

    <header class="brand">
      <div class="brand-dot" aria-hidden="true"></div>
      <div class="brand-name">Northgate<br>Exteriors</div>
    </header>

    <footer class="footer">
      <div>215 Linden Park Rd Ste 300, Fairview, MD 20900</div>
      <div>
        <span class="item"><span class="label">P:</span> 555-014-2381</span>
        <span class="item"><span class="label">F:</span> 555-014-2727</span>
        <span class="item"><span class="label">W:</span> www.northgateexteriors.com</span>
      </div>
    </footer>
  </main>
</body>
</html>
```